Landing page for new software as a service product

==== ENGLISH VERSION ====

Due to our excellent customer service, the company BrimNest has gained many satisfied customers. Now we have developed a new product, which enables companies in times of Covid-19 to use a video salesroom, to get in contact with their customers. In contrast to many other solutions on the market, it is not only an outbound solution. Our solution can handle incoming calls from the website / shop / app of a customer. The video call is routed by different rules (regarding day of week, time and sales agent) to the correct sales agent. If no sales agent is available different exit strategies are available to not loose the lead.

We need a LANDING PAGE for this application (no backend design!), Which can later be translated into different languages. Attached are screenshots of the application, which can be used if required. If you need other information, you are free to contact us and we try to provide these information to you.

==== GERMAN VERSION ====

As a cloud provider, BrimNest has gained many satisfied customers through excellent customer service in recent years. Now we have developed a new product that enables companies to make sales via video. And not just in the outbound, as known from well-known providers, but also in the inbound. This means that the customer can start a video call to the dealer using a button on the homepage. The call is then routed to the appropriate employee as with a correct telephone system according to previously defined rules (date, time, user groups).

For this application we need a landing page, which can later be translated into other languages. Screenshots of the application are included and additional ones can be created if required. As a technician, it is difficult for us to select the correct information here. So if there is a need for more information, we can certainly provide it if it is named.
Updates

I've made the mistake and made only a german briefing, which was really not suitable for the most designers. I've fixed this error and translated the briefing now.

Requirements
Must have
• A landing page design, for the new product. Please only designs which fits the topic and not some generic designs which need to be customized by us ... If we we're able to do this, we would not ask for help here ;-)
Should not have
• We do not need an admin template for the application, we already have an admin design.

```html
<!DOCTYPE html>
<html lang="en">
<head>
<meta charset="utf-8">
<title>BrimNest Video Sales – Landing Page</title>
<link href="https://fonts.googleapis.com/css2?family=Roboto:wght@300;400;500;700&display=swap" rel="stylesheet">
<style>
:root{
  --blue:#1b8fd6;
  --grey-btn:#9aa3a8;
  --dark:#333333;
  --footer:#2b2b2b;
  --text:#222;
  --muted:#777;
  --light:#f0f0f0;
  --green:#8cc34a;
  --teal:#5bb8d6;
  --line:#e3e3e3;
}
*{box-sizing:border-box;margin:0;padding:0}
html,body{width:1200px;height:4817px;overflow:hidden}
body{font-family:'Roboto',sans-serif;color:var(--text);background:#fff;position:relative}
.abs{position:absolute}
.center{text-align:center}

/* hero */
.hero{position:absolute;left:0;top:0;width:1200px;height:683px;
  background:linear-gradient(115deg,#6b3a36 0%,#9a5a52 22%,#8d8f95 45%,#c8c8c6 70%,#e9e7e2 100%)}
.hero-shade{position:absolute;inset:0;background:rgba(30,30,40,.35)}
.hero h1{position:absolute;left:0;width:1200px;top:222px;text-align:center;color:#fff;
  font-weight:300;font-size:40px;line-height:50px;text-transform:uppercase}
.hero p{position:absolute;left:190px;width:820px;top:345px;text-align:center;color:#fff;font-size:13px;line-height:21px}
.pill{position:absolute;border-radius:22px;color:#fff;font-weight:700;font-size:12px;
  text-transform:uppercase;letter-spacing:.6px;display:flex;align-items:center;justify-content:center}
.pill.blue{background:var(--blue)}
.pill.grey{background:var(--grey-btn)}
.scroll-down{position:absolute;left:568px;top:583px;width:60px;height:60px;border:2px solid rgba(255,255,255,.8);border-radius:50%}

/* features */
.section-title{position:absolute;left:0;width:1200px;text-align:center;font-weight:300;font-size:38px;color:#222}
.feature{position:absolute;width:320px;text-align:center}
.feature .num{font-size:56px;font-weight:300;color:#bdbdbd;line-height:60px}
.feature h3{font-size:14px;font-weight:700;margin-top:8px}
.feature p{font-size:13px;color:var(--muted);line-height:22px;margin-top:8px;font-weight:300}

/* band */
.band{position:absolute;left:0;top:1322px;width:1200px;height:181px;background:var(--dark)}
.band .rule{position:absolute;left:518px;width:162px;height:1px;background:#bbb}
.band p{position:absolute;left:0;width:1200px;top:60px;text-align:center;color:#fff;font-size:19px;line-height:32px}

/* icon circles */
.ring{position:absolute;width:146px;height:146px;border-radius:50%;border:9px solid #cfcfcf;background:#fff}
.ring svg{position:absolute;left:32px;top:32px}
.ring-label{position:absolute;width:180px;text-align:center;font-size:15px;font-weight:300;letter-spacing:.4px;color:#333}

/* app screens */
.app-small{font-size:7px;color:#999}
.dash-card{position:absolute;background:#f6f6f6;border:1px solid #e9e9e9}
.dash-card .cap{position:absolute;bottom:6px;width:100%;text-align:center;font-size:7px;color:#999;border-top:1px solid #e4e4e4;padding-top:5px}
.chart{position:absolute;background:#f6f6f6;border:1px solid #e9e9e9}
.panel{position:absolute;background:#fff;border:1px solid #ddd;box-shadow:0 1px 4px rgba(0,0,0,.12)}
.panel .ttl{position:absolute;left:12px;top:14px;font-size:10px;font-weight:700}
.panel .x{position:absolute;right:12px;top:12px;font-size:11px;color:#777}
.field{position:absolute;height:24px;border:1px solid #e1e1e1;font-size:9px;color:#888;padding:6px 8px}
.flabel{position:absolute;font-size:9px;color:#555}
.mini-btn{position:absolute;height:22px;font-size:8px;color:#fff;display:flex;align-items:center;justify-content:center;border-radius:2px}

/* pricing */
.pricing{position:absolute;left:0;top:3104px;width:1200px;height:673px;background:var(--light)}
.plan{position:absolute;top:150px;width:303px;height:436px;background:#fff}
.plan .price{position:absolute;left:48px;top:48px;font-size:56px;font-weight:700;color:#222}
.plan .price sup{font-size:20px;font-weight:400;vertical-align:top;position:relative;top:8px;margin-right:2px}
.plan .name{position:absolute;left:48px;top:126px;font-size:19px;font-weight:700;color:#666}
.plan p{position:absolute;left:48px;width:215px;top:208px;font-size:13px;line-height:22px;color:var(--muted);font-weight:300}
.plan .pill{left:72px;top:339px;width:159px;height:42px}

/* contact */
.clabel{position:absolute;font-size:14px;color:#444;font-weight:300}
.cinput{position:absolute;background:#fff;border:1px solid #ececec}

/* footer */
.footer{position:absolute;left:0;top:4432px;width:1200px;height:385px;background:var(--footer);color:#fff}
.footer h4{position:absolute;font-size:12px;font-weight:700;letter-spacing:.3px}
.footer p,.footer a{font-size:13px;line-height:22px;color:#fff;text-decoration:none}
.footer .links{position:absolute;left:120px;top:172px;display:flex;flex-direction:column}
.social{position:absolute;top:4682px;display:flex;gap:14px}
.social span{width:14px;height:14px;border-radius:50%;background:#8a8a8a}
</style>
</head>
<body>

<!-- HERO -->
<section class="hero">
  <div role="img" aria-label="Photo of a person holding a phone during a video call with a salesperson" style="position:absolute;inset:0"></div>
  <div class="hero-shade"></div>
  <h1>Keep your business running during<br>coronavirus (COVID-19)</h1>
  <p>In order to keep your business running we have developed solutions that will reassure your customers and enhance your performance by mitigating the Coronavirus negative business effects.</p>
  <div class="pill blue" style="left:402px;top:411px;width:187px;height:42px">Learn more</div>
  <div class="pill grey" style="left:607px;top:411px;width:191px;height:42px">Contact us</div>
  <div class="scroll-down">
    <svg width="56" height="56" viewBox="0 0 56 56"><path d="M28 17v22M19 30l9 9 9-9" stroke="#fff" stroke-width="2" fill="none"/></svg>
  </div>
</section>

<!-- WHY CHOOSE -->
<h2 class="section-title" style="top:790px">Why Choose our product?</h2>
<div class="feature" style="left:109px;top:862px"><div class="num">01.</div><h3>Easy and friendly</h3><p>Inbound calls from the homepage of the customer</p></div>
<div class="feature" style="left:438px;top:862px"><div class="num">02.</div><h3>Smart</h3><p>Inbound call routing depending on product, day of week, time</p></div>
<div class="feature" style="left:767px;top:862px"><div class="num">03.</div><h3>Time flexible</h3><p>Escalation steps if customer calls out of business hours or no agent is available, to get as much leads as possible</p></div>
<div class="feature" style="left:99px;top:1099px;width:340px"><div class="num">04.</div><h3>Mobile ready</h3><p>Forward the call to mobile devices and use the camera to show the product in detail LIVE.</p></div>
<div class="feature" style="left:438px;top:1099px"><div class="num">05.</div><h3>Follow up</h3><p>Outbound calls as a way for follow up calls</p></div>
<div class="feature" style="left:767px;top:1099px"><div class="num">06.</div><h3>Sharing is caring</h3><p>Share presentations and documents (like offers) with the customer</p></div>

<!-- BAND -->
<section class="band">
  <div class="rule" style="top:28px"></div>
  <p>Did you know? with our services, your customers can start a video<br>call to a dealer using a button on your homepage.</p>
  <div class="rule" style="top:151px"></div>
</section>

<!-- ICONS -->
<h2 class="section-title" style="top:1552px">easy, smart and friendly!</h2>
<div class="ring" style="left:166px;top:1634px"><svg width="64" height="64" viewBox="0 0 64 64"><rect x="17" y="4" width="30" height="56" rx="4" fill="none" stroke="#e23b3b" stroke-width="3"/><rect x="23" y="24" width="13" height="11" fill="none" stroke="#e23b3b" stroke-width="2.5"/><path d="M36 28l6-3v9l-6-3z" fill="#e23b3b"/></svg></div>
<div class="ring" style="left:346px;top:1634px"><svg width="64" height="64" viewBox="0 0 64 64"><path d="M12 42A22 22 0 1 1 52 42" fill="none" stroke="#4caf50" stroke-width="9"/><path d="M6 40l12 4 -2-12z" fill="#555"/></svg></div>
<div class="ring" style="left:527px;top:1634px"><svg width="64" height="64" viewBox="0 0 64 64"><path d="M10 32a22 22 0 0 1 38-15M54 32a22 22 0 0 1-38 15" fill="none" stroke="#555" stroke-width="3"/><path d="M48 8v10h-10M16 56V46h10" fill="none" stroke="#555" stroke-width="3"/><path d="M26 24c2 8 6 12 14 14l3-4-5-3-2 2c-3-1-5-3-6-6l2-2-3-5z" fill="#1b8fd6"/></svg></div>
<div class="ring" style="left:706px;top:1634px"><svg width="64" height="64" viewBox="0 0 64 64"><path d="M8 50h14l20-28h14" fill="none" stroke="#555" stroke-width="6" stroke-linejoin="round"/><circle cx="28" cy="16" r="4" fill="#1b8fd6"/><path d="M28 22v12" stroke="#1b8fd6" stroke-width="4"/></svg></div>
<div class="ring" style="left:888px;top:1634px"><svg width="64" height="64" viewBox="0 0 64 64"><path d="M6 20L22 6l36 36-16 16z" fill="none" stroke="#1b8fd6" stroke-width="3"/><circle cx="17" cy="17" r="3" fill="#1b8fd6"/><text x="30" y="36" transform="rotate(45 30 36)" font-family="Roboto,sans-serif" font-size="10" font-weight="700" fill="#1b8fd6" text-anchor="middle">BRAND</text></svg></div>
<div class="ring-label" style="left:149px;top:1792px">FOLLOW-UP CALL</div>
<div class="ring-label" style="left:329px;top:1792px">1/9 USERS</div>
<div class="ring-label" style="left:510px;top:1792px">CALL ROUTING</div>
<div class="ring-label" style="left:689px;top:1792px">ESCALATION</div>
<div class="ring-label" style="left:871px;top:1792px">BRANDING</div>

<!-- DASHBOARD SCREEN -->
<div class="abs" style="left:146px;top:1887px;width:906px;height:9px;border-bottom:1px solid #eee;font-size:5px;color:#999;display:flex;gap:30px">
  <span style="color:var(--green)">BRIMNEST VIDEO</span><span>Dashboard</span><span>Users</span><span>Routing</span><span>Calls</span><span>Reports</span><span style="margin-left:auto">Logout</span>
</div>
<div class="abs" style="left:152px;top:1917px;font-size:11px;color:var(--green)">DASHBOARD</div>
<div class="abs" style="left:47px;top:1953px;width:1140px;height:1px;background:#ddd"></div>
<div class="abs" style="left:54px;top:1974px;font-size:15px;color:#9bb55a">DASHBOARD</div>

<div class="dash-card" style="left:62px;top:2013px;width:265px;height:140px">
  <svg class="abs" style="left:116px;top:30px" width="32" height="52" viewBox="0 0 32 52"><rect x="3" y="2" width="26" height="48" rx="3" fill="none" stroke="#9bb55a" stroke-width="3"/><rect x="9" y="18" width="10" height="8" fill="none" stroke="#9bb55a" stroke-width="2"/><path d="M19 21l5-2v7l-5-2z" fill="#9bb55a"/></svg>
  <div class="cap">Follow-up calls</div></div>
<div class="dash-card" style="left:340px;top:2013px;width:267px;height:140px">
  <svg class="abs" style="left:100px;top:28px" width="70" height="60" viewBox="0 0 70 60"><path d="M12 50A25 25 0 1 1 58 50" fill="none" stroke="#bbb" stroke-width="9"/></svg>
  <div class="cap">Users online</div></div>
<div class="dash-card" style="left:622px;top:2013px;width:266px;height:140px">
  <div class="abs center" style="width:100%;top:32px;font-size:40px">0</div>
  <div class="cap">Incoming calls today</div></div>
<div class="dash-card" style="left:903px;top:2013px;width:265px;height:140px">
  <div class="abs center" style="width:100%;top:32px;font-size:40px">00:00</div>
  <div class="cap">Average call time</div></div>

<div class="chart" style="left:62px;top:2178px;width:545px;height:205px">
  <svg class="abs" style="left:0;top:0" width="545" height="205" viewBox="0 0 545 205">
    <g stroke="#e3e3e3"><line x1="22" y1="15" x2="22" y2="160"/><line x1="22" y1="160" x2="535" y2="160"/>
    <line x1="22" y1="40" x2="535" y2="40"/><line x1="22" y1="70" x2="535" y2="70"/><line x1="22" y1="100" x2="535" y2="100"/><line x1="22" y1="130" x2="535" y2="130"/></g>
    <g stroke="#eee"><line x1="80" y1="15" x2="80" y2="160"/><line x1="140" y1="15" x2="140" y2="160"/><line x1="200" y1="15" x2="200" y2="160"/><line x1="260" y1="15" x2="260" y2="160"/><line x1="320" y1="15" x2="320" y2="160"/><line x1="380" y1="15" x2="380" y2="160"/><line x1="440" y1="15" x2="440" y2="160"/><line x1="500" y1="15" x2="500" y2="160"/></g>
    <text x="272" y="198" font-size="6" fill="#999" text-anchor="middle" font-family="Roboto,sans-serif">Today calls</text>
  </svg></div>
<div class="chart" style="left:622px;top:2178px;width:546px;height:205px">
  <svg class="abs" style="left:0;top:0" width="546" height="205" viewBox="0 0 546 205">
    <g stroke="#e3e3e3"><line x1="22" y1="15" x2="22" y2="160"/><line x1="22" y1="160" x2="536" y2="160"/>
    <line x1="22" y1="40" x2="536" y2="40"/><line x1="22" y1="70" x2="536" y2="70"/><line x1="22" y1="100" x2="536" y2="100"/><line x1="22" y1="130" x2="536" y2="130"/></g>
    <g stroke="#eee"><line x1="80" y1="15" x2="80" y2="160"/><line x1="140" y1="15" x2="140" y2="160"/><line x1="200" y1="15" x2="200" y2="160"/><line x1="260" y1="15" x2="260" y2="160"/><line x1="320" y1="15" x2="320" y2="160"/><line x1="380" y1="15" x2="380" y2="160"/><line x1="440" y1="15" x2="440" y2="160"/><line x1="500" y1="15" x2="500" y2="160"/></g>
    <text x="273" y="198" font-size="6" fill="#999" text-anchor="middle" font-family="Roboto,sans-serif">Yesterday calls</text>
  </svg></div>

<div class="abs" style="left:47px;top:2407px;width:1153px;height:14px;background:#555;color:#fff;font-size:6px;text-align:right;padding:4px 14px 0 0">BACK TO TOP</div>

<!-- LEFT FORM PANEL -->
<div class="panel" style="left:47px;top:2446px;width:603px;height:471px">
  <div class="ttl" style="color:var(--green)">CREATE NEW CALL FLOW</div><div class="x">×</div>
  <svg class="abs" style="left:12px;top:64px" width="580" height="38" viewBox="0 0 580 38">
    <path d="M0 0h190l12 19-12 19H0z" fill="#8cc34a"/><path d="M190 0h192l12 19-12 19H190l12-19z" fill="#7cb342"/><path d="M382 0h190l8 19-8 19H382l12-19z" fill="#6cc3e0"/>
    <g font-family="Roboto,sans-serif" font-size="8" fill="#fff"><text x="40" y="16">Basic informations</text><text x="40" y="28" font-size="6">Times and Description</text>
    <text x="250" y="16">Call Routing</text><text x="240" y="28" font-size="6">Who should receive calls</text>
    <text x="444" y="16">Escalation</text><text x="434" y="28" font-size="6">Where to send the user</text></g>
  </svg>
  <div class="abs" style="left:50px;top:146px;width:500px;font-size:8px;line-height:12px;color:#444">If on your side nobody is available for a call or the call is made outside the available hours, the user should be routed to a place where he can leave a message or find what he needs. Please specify in this step the url, where the user should be redirected to if nobody answers his call.</div>
  <div class="flabel" style="left:50px;top:186px">Exit URL</div><div class="field" style="left:50px;top:200px;width:505px">URL</div>
  <div class="flabel" style="left:50px;top:246px">Out of business hours URL</div><div class="field" style="left:50px;top:260px;width:505px">URL</div>
  <div class="flabel" style="left:50px;top:306px">Escalation URL</div><div class="field" style="left:50px;top:320px;width:505px">URL</div>
  <div class="mini-btn" style="left:436px;top:437px;width:60px;background:var(--teal)">Previous</div>
  <div class="mini-btn" style="left:500px;top:437px;width:40px;background:#a9d8e8">Next</div>
  <div class="mini-btn" style="left:544px;top:437px;width:40px;background:var(--teal)">Save</div>
</div>

<!-- RIGHT FORM PANEL -->
<div class="panel" style="left:677px;top:2446px;width:510px;height:621px">
  <div class="ttl" style="color:var(--teal)">CREATE NEW CALL FLOW</div><div class="x">×</div>
  <svg class="abs" style="left:12px;top:56px" width="486" height="32" viewBox="0 0 486 32">
    <path d="M0 0h160l10 16-10 16H0z" fill="#5bb8d6"/><path d="M160 0h165l10 16-10 16H160l10-16z" fill="#eef6fa"/><path d="M325 0h161v32H325l10-16z" fill="#eef6fa"/>
    <g font-family="Roboto,sans-serif" font-size="7"><text x="30" y="13" fill="#fff">Basic informations</text><text x="30" y="24" fill="#fff" font-size="5">Times and Description</text>
    <text x="220" y="13" fill="#999">Call Routing</text><text x="210" y="24" fill="#bbb" font-size="5">Who should receive calls</text>
    <text x="382" y="13" fill="#999">Escalation</text><text x="372" y="24" fill="#bbb" font-size="5">Where to send the user</text></g>
  </svg>
  <div class="abs" style="left:42px;top:110px;width:430px;font-size:7px;line-height:10px;color:#444">To provide a better customer journey you can create multiple call flows. Every call flow will route an incoming video call according to its specifications. In this first step, please provide a short name to identify the call flow and times when this call flow should be active.</div>
  <div class="flabel" style="left:42px;top:152px;font-size:7px">Name</div><div class="field" style="left:42px;top:164px;width:210px;height:20px;font-size:7px;padding:4px 6px">Name</div>
  <div class="flabel" style="left:258px;top:152px;font-size:7px">Description</div><div class="field" style="left:258px;top:164px;width:214px;height:20px;font-size:7px;padding:4px 6px">Description</div>
  <svg class="abs" style="left:42px;top:204px" width="440" height="300" viewBox="0 0 440 300" font-family="Roboto,sans-serif" font-size="7">
    <g font-weight="700" fill="#333"><text x="6" y="8">Day of Week</text><text x="76" y="8">Start Time</text><text x="258" y="8">End Time</text></g>
    <g fill="#555">
      <text x="6" y="42">Monday</text><text x="6" y="80">Tuesday</text><text x="6" y="118">Wednesday</text><text x="6" y="156">Thursday</text><text x="6" y="194">Friday</text><text x="6" y="232">Saturday</text><text x="6" y="270">Sunday</text>
    </g>
    <g fill="none" stroke="#e1e1e1">
      <rect x="76" y="30" width="170" height="20"/><rect x="256" y="30" width="170" height="20"/>
      <rect x="76" y="68" width="170" height="20"/><rect x="256" y="68" width="170" height="20"/>
      <rect x="76" y="106" width="170" height="20"/><rect x="256" y="106" width="170" height="20"/>
      <rect x="76" y="144" width="170" height="20"/><rect x="256" y="144" width="170" height="20"/>
      <rect x="76" y="182" width="170" height="20"/><rect x="256" y="182" width="170" height="20"/>
      <rect x="76" y="220" width="170" height="20"/><rect x="256" y="220" width="170" height="20"/>
      <rect x="76" y="258" width="170" height="20"/><rect x="256" y="258" width="170" height="20"/>
    </g>
    <g fill="#666">
      <text x="82" y="43">00:00</text><text x="262" y="43">00:00</text><text x="82" y="81">00:00</text><text x="262" y="81">00:00</text>
      <text x="82" y="119">00:00</text><text x="262" y="119">00:00</text><text x="82" y="157">00:00</text><text x="262" y="157">00:00</text>
      <text x="82" y="195">00:00</text><text x="262" y="195">00:00</text><text x="82" y="233">00:00</text><text x="262" y="233">00:00</text>
      <text x="82" y="271">00:00</text><text x="262" y="271">00:00</text>
    </g>
    <g fill="none" stroke="#aaa"><circle cx="236" cy="40" r="4"/><circle cx="416" cy="40" r="4"/><circle cx="236" cy="78" r="4"/><circle cx="416" cy="78" r="4"/><circle cx="236" cy="116" r="4"/><circle cx="416" cy="116" r="4"/><circle cx="236" cy="154" r="4"/><circle cx="416" cy="154" r="4"/><circle cx="236" cy="192" r="4"/><circle cx="416" cy="192" r="4"/><circle cx="236" cy="230" r="4"/><circle cx="416" cy="230" r="4"/><circle cx="236" cy="268" r="4"/><circle cx="416" cy="268" r="4"/></g>
  </svg>
  <div class="mini-btn" style="left:370px;top:582px;width:46px;height:18px;background:#a9d8e8">Previous</div>
  <div class="mini-btn" style="left:420px;top:582px;width:32px;height:18px;background:var(--teal)">Next</div>
  <div class="mini-btn" style="left:456px;top:582px;width:32px;height:18px;background:#a9d8e8">Save</div>
</div>

<!-- PRICING -->
<section class="pricing">
  <h2 class="section-title" style="top:34px">check out our businesses plans!</h2>
  <div class="plan" style="left:120px"><div class="price"><sup>€</sup>75</div><div class="name">Standard,</div>
    <p>This monthly payment option includes for 10 concurrent users in a video call (plus taxes, if applicable).</p><div class="pill blue">Buy now</div></div>
  <div class="plan" style="left:449px"><div class="price"><sup>€</sup>84</div><div class="name">Business</div>
    <p>Montly plan. For every additional, concurrent video call user will be 9€ ( plus taxes, if applicable).</p><div class="pill blue">Buy now</div></div>
  <div class="plan" style="left:778px"><div class="price"><sup>€</sup>250</div><div class="name">Ilimited</div>
    <p>Montly payment. Get unlimited users by subscribing our ilimited plan and save money!</p><div class="pill blue">Buy now</div></div>
</section>

<!-- CONTACT -->
<h2 class="section-title" style="top:3870px">CONTACT US</h2>
<div class="clabel" style="left:275px;top:3976px">Name</div><div class="cinput" style="left:275px;top:4004px;width:198px;height:50px"></div>
<div class="clabel" style="left:501px;top:3976px">Email</div><div class="cinput" style="left:501px;top:4004px;width:196px;height:50px"></div>
<div class="clabel" style="left:725px;top:3976px">Phone</div><div class="cinput" style="left:725px;top:4004px;width:198px;height:50px"></div>
<div class="clabel" style="left:275px;top:4071px">Message</div><div class="cinput" style="left:275px;top:4099px;width:648px;height:180px"></div>
<div class="pill blue" style="left:535px;top:4301px;width:129px;height:42px">Send</div>

<!-- FOOTER -->
<footer class="footer">
  <h4 style="left:365px;top:44px">RECENT NEWS</h4>
  <p class="abs" style="left:365px;top:82px;width:300px">Lorem ipsum dolor sit amet, consectetur adipiscing elit, sed do eiusmod tempor incididunt ut labore et dolore magna aliqua. Ut enim ad minim veniam, quis nostrud exercitation ullamco laboris nisi ut aliquip ex ea commodo consequat.</p>
  <h4 style="left:778px;top:44px">SUBSCRIBE</h4>
  <p class="abs" style="left:778px;top:82px">Get monthly updates and free resources.</p>
  <div class="abs" style="left:793px;top:150px;width:140px;height:36px;border-radius:18px;background:#fff;color:#999;font-size:10px;display:flex;align-items:center;justify-content:center">Email</div>
  <div class="pill blue" style="left:926px;top:150px;width:132px;height:36px">Subscribe</div>
  <h4 style="left:778px;top:224px">CONNECT WITH US</h4>
  <h4 style="left:120px;top:142px">BRIMNEST</h4>
  <div class="links"><a>About Us</a><a>Services</a><a>Selected Work</a><a>Get In Touch</a></div>
  <p class="abs" style="left:120px;top:328px;font-size:12px">© BRIMNEST - All Rights Reserved</p>
</footer>
<div class="social" style="left:785px"><span></span><span></span><span></span><span></span><span></span><span></span></div>

</body>
</html>
```